Re-Design Website

Task Outline:
Re- Web design with call-to-action orientated .
Task Description:
■Our Service
Our service is call Zelvoria.
We are a mobile games only cross promotion and advertising platform.
■Reference WebSites
This will be few sites that is doing almost similar service
1.www.plumvexa.com
2.www.norquibe.com
3.www.duskorelo.net/ (japanese site, but don’t worry about the wordings.)
4.http://vintrosk.com/
■ Little Details
In a nutshell, we are advertising company for mobile games, which offer to show fullscreen ads(interstitial ads), standard banner ads, larger banner ads, icon ads and recommendation ads.
Our current site is at www.zelvoria.net. (No copy write job has been done for contents yet, don’t worry about that)
Requirements:
● flat design, play well with white space ( we love the halbrimo.com design )
● A straight to the point landing image
● All contents are fit in a 1 long page -Once scrolled down to contents. It needs to be very neat and clear on how it deliver the message through images and contents.
● Clean, simple. Reduce wordings; focus on graphic-information to intrigue response.
● We would like to reduce navigation activities and to have an outstanding Call To Action (CTA) button, which to convert user into conversion funnel (example, Learn More, to download our eBooks, Sign Up Now, Join)
● Interesting Facebook/Twitter button to build variability.
● Desired user experience, that able to convert information to graphical content. (Like above the fold like Vintrosk.com)
Please refer to a few reference images:
1. *upload a few sushi/ice cream/reon/images for them to use”
Pages to design
1. Landing page
2. About Us
3. Sign in & Sign Up (Must be simple and friendly)
Logo:
We are open to suggestions.
Color preference: (We open for suggestions) ---> WE ARE NOT GOING TO USE ORANGE
● color – change corporate Identity color. The background color can be darker above to fold to make it more stylish.
● 3 tone colors on a web page (something like halbrimo.com) → For Example (Refering to Hal Brimo : Main Color : Blue, Base Color : Gray… White, Tone Color : Green) ---> Sure you can play around with it.
● fun and energetic color tone (since we are strongly related with mobile games)
Font:
● clear typography - similar to product identity
● helvetica neue light (currently are using but we are open to suggestion)
Target Market:
● Game publisher
● Game Developer
● Partners: Advertising Agencies, (Business 2 Business)
● ASEAN Countries. ie Taiwan, Japan, China, HK...etc
Deadline:
● 31st December 2013

```html
<!DOCTYPE html>
<html lang="en">
<head>
<meta charset="utf-8">
<title>Zelvoria – Sign up</title>
<link href="https://fonts.googleapis.com/css2?family=Roboto:wght@300;400;500;700&display=swap" rel="stylesheet">
<style>
:root{
  --stage:#666666;
  --navy:#2c3e50;
  --navy-deep:#2b3d50;
  --blue:#3498db;
  --band:#3a98d8;
  --red:#e74c3c;
  --white:#ffffff;
  --ink:#111111;
  --muted:#8fa0b0;
  --field-line:#cfd6dc;
  --body-text:#333333;
}
*{box-sizing:border-box;margin:0;padding:0}
html,body{width:1200px;height:1000px;overflow:hidden}
body{background:var(--stage);font-family:"Roboto",Helvetica,Arial,sans-serif;position:relative}
.page{position:absolute;left:284px;top:0;width:632px;height:1000px;background:var(--white)}
.page *{position:absolute}
.header{left:0;top:0;width:632px;height:54px;background:var(--navy)}
.brand{left:56px;top:22px;font-size:22px;font-weight:300;color:var(--white);letter-spacing:-.3px;display:flex;align-items:center;gap:6px;position:absolute}
.brand-dot{position:static;width:8px;height:8px;border-radius:50%;background:var(--blue)}
.nav-link{top:34px;font-size:11px;font-weight:300;color:#aab6c2}
.btn{display:flex;align-items:center;justify-content:center;color:var(--white);font-weight:500;border-radius:2px}
.btn-blue{background:var(--blue)}
.btn-red{background:var(--red)}
.btn-dark{background:var(--navy);font-size:7px;font-weight:700}
.headline{left:68px;top:110px;font-size:22px;line-height:28px;font-weight:300;color:var(--navy)}
.field{top:220px;height:21px;border:1px solid var(--field-line);border-radius:3px;font-size:7px;color:#9aa5af;padding:6px 6px}
.select{left:439px;top:219px;width:123px;height:21px;background:var(--navy);border-radius:2px;color:var(--white);font-size:7px;padding:6px 6px}
.select-arrow{right:0;top:0;width:22px;height:21px;border-left:1px solid #4a5d70}
.feature-icon{top:394px;width:54px;height:54px}
.feature-title{top:455px;width:168px;text-align:center;font-size:15.5px;line-height:19px;font-weight:700;color:var(--navy)}
.feature-text{top:500px;width:168px;text-align:center;font-size:7.2px;line-height:13px;color:var(--body-text)}
.statement{left:70px;top:568px;width:492px;text-align:center;font-size:15px;line-height:19px;font-weight:500;color:var(--ink)}
.band{left:0;top:688px;width:632px;height:253px;background:var(--band)}
.card{top:681px;width:114px;height:202px;background:var(--white);border:1px solid var(--navy);border-radius:3px}
.card-art{left:3px;top:3px;width:106px;height:92px}
.card-title{left:4px;width:104px;text-align:center;font-size:10px;line-height:13px;font-weight:700;color:var(--navy)}
.card-text{left:8px;top:127px;width:96px;text-align:center;font-size:6.5px;line-height:8.5px;color:#555}
.card-btn{left:26px;top:173px;width:61px;height:18px}
.footer{left:0;top:941px;width:632px;height:59px;background:var(--navy)}
.copyright{left:74px;top:28px;font-size:6.5px;color:#8a99a8}
.badge{top:18px;width:32px;height:26px}
.btn-outline{left:449px;top:21px;width:51px;height:17px;border:1px solid var(--white);border-radius:2px;color:var(--white);font-size:7px;font-weight:700;display:flex;align-items:center;justify-content:center}
</style>
</head>
<body>
<main class="page">
  <header class="header">
    <div class="brand"><span class="brand-dot"></span>Zelvoria</div>
    <span class="nav-link" style="left:289px">about</span>
    <span class="nav-link" style="left:342px">how it works</span>
    <span class="nav-link" style="left:426px">applications</span>
    <a class="btn btn-blue" style="left:513px;top:31px;width:50px;height:17px;font-size:7px">Sign up</a>
  </header>

  <h1 class="headline">Sign up to your favourite in-app<br>monetization service</h1>

  <div class="field" style="left:68px;width:208px">Name</div>
  <div class="field" style="left:295px;width:124px">Email</div>
  <div class="select">Industry
    <span class="select-arrow"><svg width="22" height="21" viewBox="0 0 22 21"><path d="M7 8h8l-4 5z" fill="#fff"/></svg></span>
  </div>
  <a class="btn btn-red" style="left:68px;top:264px;width:92px;height:23px;font-size:9px">Sign up</a>

  <svg class="feature-icon" style="left:119px" viewBox="0 0 54 54" aria-label="Calendar icon">
    <rect x="7" y="5" width="40" height="40" fill="#2f6fb4"/>
    <rect x="11" y="9" width="32" height="32" fill="#f3f3f3"/>
    <rect x="11" y="9" width="32" height="5" fill="#dcdcdc"/>
    <text x="27" y="37" text-anchor="middle" font-family="Roboto,sans-serif" font-weight="700" font-size="20" fill="#e74c3c">1</text>
  </svg>
  <svg class="feature-icon" style="left:287px" viewBox="0 0 54 54" aria-label="Infinity icon">
    <circle cx="27" cy="27" r="26" fill="#2f7fc1"/>
    <path d="M27 27c-4-6-13-8-13 0s9 6 13 0 13-8 13 0-9 6-13 0z" fill="none" stroke="#f1c40f" stroke-width="4.5"/>
  </svg>
  <div class="feature-icon" style="left:456px;border-radius:50%;background:conic-gradient(#8e44ad 0 25%,#27ae60 25% 45%,#2980b9 45% 65%,#e67e22 65% 85%,#c0392b 85% 100%)" role="img" aria-label="Colourful customisation emblem"></div>

  <h2 class="feature-title" style="left:62px">First day<br>monetization</h2>
  <h2 class="feature-title" style="left:230px">Recurring<br>items</h2>
  <h2 class="feature-title" style="left:399px">Great<br>customisation</h2>
  <p class="feature-text" style="left:62px">Lorem ipsum dolor sit amet, consectetur adipiscing elit. Cras imperdiet pharetra erat, sed vulputate mauris mattis sed.</p>
  <p class="feature-text" style="left:230px">Lorem ipsum dolor sit amet, consectetur adipiscing elit. Cras imperdiet pharetra erat, sed vulputate mauris mattis sed.</p>
  <p class="feature-text" style="left:399px">Lorem ipsum dolor sit amet, consectetur adipiscing elit. Cras imperdiet pharetra erat, sed vulputate mauris mattis sed.</p>

  <p class="statement">Lorem ipsum dolor sit amet, consectetur adipiscing elit. Cras im-perdiet pharetra erat, sed vulputate mauris mattis sed.</p>
  <a class="btn btn-blue" style="left:257px;top:623px;width:122px;height:23px;font-size:9px;font-weight:400">Download e-book</a>

  <section class="band"></section>

  <article class="card" style="left:69px">
    <div class="card-art" role="img" aria-label="Game scene with an ice cream shop and cartoon staff" style="background:linear-gradient(#f3d6c4,#c9715a)"></div>
    <h3 class="card-title" style="top:112px">Fullscreen ads</h3>
    <p class="card-text">Lorem ipsum dolor sit amet, consectetur adipiscing elit. Cras imperdiet pharetra erat, sed vulputate mauris mattis</p>
    <a class="btn btn-dark card-btn">How it works</a>
  </article>
  <article class="card" style="left:195px">
    <div class="card-art" role="img" aria-label="Sushi game banner artwork" style="background:linear-gradient(#f2f2f2,#d9534f);height:70px"></div>
    <h3 class="card-title" style="top:96px">Standard and<br>larger ads</h3>
    <p class="card-text">Lorem ipsum dolor sit amet, consectetur adipiscing elit. Cras imperdiet pharetra erat, sed vulputate mauris mattis</p>
    <a class="btn btn-dark card-btn">How it works</a>
  </article>
  <article class="card" style="left:322px">
    <div class="card-art" role="img" aria-label="Game app icon artwork" style="left:9px;top:8px;width:94px;height:90px;border-radius:14px;background:linear-gradient(#7fd3c4,#3fa99a)"></div>
    <h3 class="card-title" style="top:112px">Icon ads</h3>
    <p class="card-text">Lorem ipsum dolor sit amet, consectetur adipiscing elit. Cras imperdiet pharetra erat, sed vulputate mauris mattis</p>
    <a class="btn btn-dark card-btn">How it works</a>
  </article>
  <article class="card" style="left:449px">
    <div class="card-art" role="img" aria-label="Ice cream game promotional artwork" style="background:linear-gradient(#f7dede,#b5503a)"></div>
    <h3 class="card-title" style="top:112px">Recommandations</h3>
    <p class="card-text">Lorem ipsum dolor sit amet, consectetur adipiscing elit. Cras imperdiet pharetra erat, sed vulputate mauris mattis</p>
    <a class="btn btn-dark card-btn">How it works</a>
  </article>

  <footer class="footer">
    <span class="copyright">Copyright 2014 (c) Zelvoria</span>
    <svg class="badge" style="left:270px" viewBox="0 0 32 26" aria-label="Social badge"><circle cx="16" cy="13" r="12" fill="#3b5b9a" stroke="#cfd8e3" stroke-width="2"/></svg>
    <svg class="badge" style="left:332px" viewBox="0 0 32 26" aria-label="Social badge"><circle cx="16" cy="13" r="12" fill="#3a9bd9" stroke="#cfd8e3" stroke-width="2"/></svg>
    <a class="btn-outline">About us</a>
    <a class="btn btn-blue" style="left:513px;top:21px;width:50px;height:17px;font-size:7px">Sign up</a>
  </footer>
</main>
</body>
</html>
```